Vesk Architecture

We are a architectural design and build company working between scales 1/1000 to 1/1 we want people to understand our difference from our design experience and quality.we build hotels restourants and office spaces.Our company name is Vesk architecture to mind sustainability.

We want to write our adress phone and work spesifications on the card and we want our logo as backround.

Ps:you could find the logo adress and phone box numbers from the web:www.veskmimarlik-ornek.com

Target Market(s)

Who looks for experts.

Industry/Entity Type

Architecture

Requirements
Must have
• Design is over everything.
Should not have
• we don want it to be colorfull

```html
<!DOCTYPE html>
<html lang="en">
<head>
<meta charset="utf-8">
<title>Vesk Mimarlık — Business Card</title>
<link rel="stylesheet" href="https://fonts.googleapis.com/css2?family=PT+Sans:wght@400&display=swap">
<style>
  :root {
    --backdrop: #eeeeee;
    --card: #ffffff;
    --ink: #111111;
    --name: #555555;
    --role: #6a8fbf;
    --detail: #8a8a8a;
    --rule: #cfcfcf;
    --mist: #e4e8ee;
    --band: #000000;
  }
  * { margin: 0; padding: 0; box-sizing: border-box; }
  html, body {
    width: 1200px;
    height: 1118px;
    overflow: hidden;
    background: var(--backdrop);
    font-family: "PT Sans", sans-serif;
  }
  .canvas {
    position: relative;
    width: 1200px;
    height: 1118px;
  }
  .card {
    position: absolute;
    left: 343px;
    top: 78px;
    width: 519px;
    height: 945px;
    background: var(--card);
    overflow: hidden;
  }
  .brand-name {
    position: absolute;
    top: 190px;
    left: 0;
    width: 100%;
    text-align: center;
    font-size: 70px;
    font-weight: 400;
    color: var(--ink);
    letter-spacing: 1px;
  }
  .person {
    position: absolute;
    top: 378px;
    width: 100%;
    text-align: center;
  }
  .person-name {
    font-size: 32px;
    color: var(--name);
    line-height: 44px;
  }
  .person-role {
    font-size: 31px;
    color: var(--role);
    line-height: 44px;
  }
  .divider {
    position: absolute;
    top: 493px;
    left: 104px;
    width: 310px;
    height: 2px;
    background: linear-gradient(to right, transparent, var(--rule) 20%, var(--rule) 80%, transparent);
  }
  .contact {
    position: absolute;
    z-index: 2;
    top: 560px;
    width: 100%;
    text-align: center;
    list-style: none;
    font-size: 25px;
    line-height: 30.5px;
    color: var(--detail);
  }
  .mist {
    position: absolute;
    z-index: 1;
    left: 0;
    top: 700px;
    width: 100%;
    height: 69px;
    background: linear-gradient(to bottom, var(--card), var(--mist));
  }
  .band {
    position: absolute;
    left: 0;
    top: 769px;
    width: 100%;
    height: 176px;
    background: var(--band);
  }
</style>
</head>
<body>
  <main class="canvas">
    <article class="card">
      <h1 class="brand-name">Vesk Mimarlık</h1>
      <section class="person">
        <p class="person-name">Dana Voicu</p>
        <p class="person-role">Manager</p>
      </section>
      <div class="divider"></div>
      <ul class="contact">
        <li>0711 222 333</li>
        <li>yourname@veskmimarlik-ornek.com</li>
        <li>www.veskmimarlik-ornek.com</li>
        <li>no 25 street</li>
      </ul>
      <div class="mist"></div>
      <div class="band"></div>
    </article>
  </main>
</body>
</html>
```